Business Card and Letterhead for Vantage Psychology

We need a business card design and letterhead to use for our Psychology firm that specializes in psychoeducational assessments and individual therapy. Our motto is Purpose-Driven Assessments, Meaning-Centered Therapy.Our contact information is as follows:
Vantage Psychology
The Marwick Block - 6127-48St.
Box 2716 Ashcombe, WR
T2K 3M8
t 403.555.0148 (VANT)
f 403.555.0172
www.vantagepsychology-example.ca
The business card will be used for two different psychologists so I can supply names nearer to completion. We prefer clean, uncluttered looks.

Target Market(s)

Clients, Educators

Font styles to use
Sans Serif

Colors

Designer to choose colors to be used in the design.

Requirements
Must have
• All relevant contact info, logo, some "white" space.
Nice to have
• It would be nice to see letterhead options that have the logo on the top of the page but also options that have it on the side. I think top of the page is probably our preference.
Should not have
• Too much clutter!

```html
<!DOCTYPE html>
<html lang="en">
<head>
<meta charset="utf-8">
<title>Vantage Psychology Letterhead</title>
<link href="https://fonts.googleapis.com/css2?family=Roboto:wght@400;500&display=swap" rel="stylesheet">
<style>
  :root {
    --backdrop: #e9e9eb;
    --paper: #ffffff;
    --brand-blue: #3aa6c9;
    --brand-orange: #e08f2c;
    --ink: #3b3b3f;
    --ink-soft: #4a4a4f;
    --signature-tone: #d9d9dc;
  }
  * { margin: 0; padding: 0; box-sizing: border-box; }
  html, body {
    width: 1179px;
    height: 1200px;
    overflow: hidden;
    background: var(--backdrop);
  }
  .letterhead {
    position: absolute;
    left: 159px;
    top: 37px;
    width: 640px;
    height: 836px;
    background: var(--paper);
    transform: scale(1.345);
    transform-origin: top left;
    font-family: "Roboto", Arial, sans-serif;
    color: var(--ink);
    box-shadow: 0 2px 10px rgba(0,0,0,0.12);
  }
  .edge-bands {
    position: absolute;
    left: 0;
    top: 0;
  }
  .brand {
    position: absolute;
    top: 118px;
    left: 0;
    width: 640px;
    display: flex;
    justify-content: center;
    align-items: center;
    gap: 8px;
  }
  .brand-dot {
    width: 14px;
    height: 14px;
    border-radius: 50%;
    background: var(--brand-blue);
  }
  .brand-name {
    font-size: 15px;
    font-weight: 500;
    letter-spacing: 0.8px;
    text-transform: uppercase;
    color: var(--brand-blue);
  }
  .letter-title {
    position: absolute;
    left: 66px;
    top: 203px;
    font-size: 14px;
    font-weight: 400;
    color: var(--ink);
  }
  .letter-body {
    position: absolute;
    left: 63px;
    top: 268px;
    width: 531px;
    font-size: 8.4px;
    line-height: 11.5px;
    text-align: justify;
    color: var(--ink-soft);
  }
  .letter-body p { margin-bottom: 11.5px; }
  .contact-block {
    position: absolute;
    left: 63px;
    top: 713px;
    font-size: 9.6px;
    line-height: 12.6px;
    font-style: normal;
    color: var(--ink);
  }
  .contact-block .gap { height: 12.6px; }
  .signature-area {
    position: absolute;
    left: 420px;
    top: 688px;
    width: 160px;
    height: 44px;
    border-radius: 4px;
    background: linear-gradient(90deg, var(--signature-tone), #ececee);
  }
</style>
</head>
<body>
  <main class="letterhead">
    <svg class="edge-bands" width="24" height="836" viewBox="0 0 24 836" aria-hidden="true">
      <rect class="band-blue" x="0" y="0" width="16" height="650" fill="var(--brand-blue)"/>
      <polygon class="band-orange" points="0,645 23,662 23,836 0,836" fill="var(--brand-orange)"/>
    </svg>

    <header class="brand">
      <span class="brand-dot"></span>
      <span class="brand-name">Vantage Psychology</span>
    </header>

    <h1 class="letter-title">Lorem ipsum</h1>

    <section class="letter-body">
      <p>Lorem ipsum dolor sit amet, consectetur adipiscing elit. In mollis ac leo sit amet commodo. Mæcenas viverra sem turpis. Nam aliquam risus ipsum, sit amet fermentum erat varius ac. Mæcenas rutrum rhoncus molestie. Præsent nisi neque, porttitor vel felis nec, ullamcorper feugiat eros. Ut vulputate mi sem, ut sodales odio accumsan sed. Cras ut nunc a lacus rhoncus ultrices. Donec eu nunc vel augue aliquam ullamcorper. Pellentesque volutpat nulla id luctus sodales. Duis quis dolor malesuada magna tristique auctor. Mæcenas fermentum vestibulum rhoncus. Aliquam erat volutpat. Nam interdum rhoncus augue nec tristique. Pellentesque efficitur finibus lectus volutpat facilisis. Fusce ut turpis ultricies, ornare nisi at, lacinia augue. Sed consectetur urna nibh, id scelerisque enim finibus vitæ.</p>
      <p>Quisque elementum erat vitæ metus tincidunt dapibus. Duis sit amet nunc eget tortor pharetra commodo at sit amet nunc. Cras at nisi massa. Proin consectetur porta augue a fermentum. Etiam feugiat, ligula eget efficitur molestie, nunc diam lacinia sem, eu lacinia leo mauris id elit. Class aptent taciti sociosqu ad litora torquent per conubia nostra, per inceptos himenæos. Duis vestibulum tempor auctor. Aliquam fringilla vestibulum turpis at aliquet. Aliquam tristique suscipit mauris quis ullamcorper. Vestibulum volutpat tempus leo, non tincidunt leo condimentum vel. Aenean ut augue non libero porttitor dignissim. Nulla arcu justo, ornare eu tortor in, rutrum convallis diam. Quisque ac posuere odio.</p>
      <p>Donec a lacus tellus. Duis tempus et sem ac commodo. Quisque posuere, turpis id egestas convallis, metus magna sollicitudin arcu, ut accumsan nibh sem at nunc. Pellentesque eleifend justo ac sapien ultrices maximus. Præsent non magna ut ante pellentesque fermentum vitæ id mi. Donec pretium est a turpis suscipit porttitor. Ut et lectus imperdiet nibh dignissim egestas consequat id arcu. Nulla vitæ purus ipsum. Fusce nec efficitur nulla, non venenatis ligula. Vestibulum in orci hendrerit, ullamcorper odio at, sodales nibh. Mæcenas at diam nec est euismod tristique. Aenean semper erat ante, vitæ commodo dui convallis ut. Nulla odio lacus, egestas et felis in, posuere ullamcorper enim.</p>
      <p>Sed nulla diam, accumsan ut auctor eu, interdum a ligula. Mæcenas vitæ luctus dolor. Morbi odio massa, euismod et vehicula in, tincidunt sit amet velit. Morbi in tempus turpis. Integer vel mi id ex ornare scelerisque. Sed vehicula dictum neque, eu vulputate sem hendrerit ut. Nulla facilisi. Sed tellus sem, imperdiet sed lobortis id, dictum non velit. Donec a nulla scelerisque elit varius auctor. Curabitur aliquam, ex id blandit viverra, lacus ipsum ornare felis, et fringilla dui ante ac turpis.</p>
      <p>Duis elit nibh, euismod vitæ pretium in, tincidunt ac nibh. Suspendisse tincidunt sapien sapien, id elementum dui aliquet ac. Mæcenas vestibulum lacinia orci at faucibus. Donec nisi dui, convallis at neque ac, tristique porttitor dui. Fusce vel ante erat. Etiam ac turpis est. Pellentesque et orci odio. Phasellus pretium sem non nunc interdum volutpat. Aliquam vel ante quis nisl rhoncus efficitur consectetur nec mauris. Donec sagittis mauris et ipsum iaculis convallis.</p>
    </section>

    <div class="signature-area" role="img" aria-label="Handwritten signature"></div>

    <address class="contact-block">
      <div>The Marwick Block - 6127-48St.</div>
      <div>Box 2716 Ashcombe, WR</div>
      <div>T2K 3M8</div>
      <div class="gap"></div>
      <div>Tel - 403.555.0148 (VANT)</div>
      <div>Fax - 403.555.0172</div>
      <div>www.vantagepsychology-example.ca</div>
    </address>
  </main>
</body>
</html>
```